Stationary Design for Quince consultant and support company

We need new stationary designed for a London based support company that provide on-site and remote support services for Quince products. Our clients are both consumers and businesses.

We would like a letterhead, compliment slip, business card and possibly an e-mail signature designed.

Business card designs can be either 1 side or 2, depending on designs we receive we may choose a preference for 1 or 2 sides later on in the design stage.

Designs needs to be at least 300dpi and should be done using CMYK colours.

We want the design to be bold, easy to read, clean and professional.

We have attached our company logo in 2 colour variations (if you need any other source files then please ask).

Our logo colours are as follows:

Blue (85, 50, 0, 0) and Green (50, 0, 100, 0)

We use two different suppliers for out stationary so here are the size dimensions for both. Unfortunately they are ever so slightly different size wise so hopefully we can get something that accommodates both, we can provide dimensions if required for final versions.

Some fonts that have been used before with our company are Probert (for tagline on our company logo) and previously had Nauman used, however we are very much open to seeing what the designers come up with and the fonts mentioned are not a requirement.
Updates

Company details for designs (however the template should be editable for multiple staff) Vorn-Q Ltd. Registered Office: 62-78 Harrowfield Lane London N7 3RB 020 7915 3381 www.vorn-q.example info@vorn-q.example Company is Registered in England and Wales Company No. 06513249 Directors details (if you want to make the template using his details), rest of the details are as above Dan Price Director dan@vorn-q.example

Hi all, Thank you for your submissions so far. Could we please ask that you don't use the logo with the tagline from our website for the stationary designs and only the logos provided in the design brief. For the business cards we are looking at normal rectangular business cards to be used and we can provide a template guide for size if needed, please just ask. Regards Vorn-Q Team

Target Market(s)

Our target market are consumers (of all ages) and small/medium businesses.

Industry/Entity Type

Business

Font styles to use
Serif
Sans Serif

Requirements
Must have
• At least business card, letterhead and compliment slip submitted (we need all 3 designed this time round)
Should not have
• Business cards should not have the writing "registered office" (letterheads and compliment slips can along the bottom edge)

```html
<!DOCTYPE html>
<html lang="en">
<head>
<meta charset="utf-8">
<title>Vorn-Q Stationery</title>
<link rel="stylesheet" href="https://fonts.googleapis.com/css2?family=Quicksand:wght@400;500;700&display=swap">
<style>
  :root {
    --bg: #ecebe8;
    --paper: #ffffff;
    --ink: #2b2b2b;
    --ink-soft: #555a60;
    --brand-blue: #4a6fc0;
    --brand-green: #7bc142;
    --lavender: #c9cee0;
    --green-wash: #dfeccc;
  }
  * { box-sizing: border-box; margin: 0; padding: 0; }
  html, body { width: 1200px; height: 1000px; overflow: hidden; }
  body {
    background: var(--bg);
    font-family: "Quicksand", sans-serif;
    color: var(--ink);
    position: relative;
  }
  .sheet {
    position: absolute;
    background: var(--paper);
    overflow: hidden;
    box-shadow: 0 2px 6px rgba(0,0,0,.12);
  }
  .wash { position: absolute; }
  .wash--corner {
    background:
      linear-gradient(225deg, var(--brand-green) 0%, rgba(123,193,66,.35) 30%, rgba(201,206,224,.7) 55%, rgba(255,255,255,0) 78%);
  }
  .wash--low {
    background:
      linear-gradient(45deg, var(--green-wash) 0%, rgba(201,206,224,.75) 35%, rgba(255,255,255,0) 70%);
  }
  .wordmark {
    position: absolute;
    display: flex;
    align-items: center;
    gap: 6px;
    font-weight: 700;
    color: var(--ink);
    letter-spacing: .08em;
    text-transform: uppercase;
  }
  .wordmark__dot { background: var(--brand-green); display: block; }

  /* Letterhead */
  .letterhead { left: 115px; top: 185px; width: 480px; height: 680px; }
  .letterhead .wash--corner { right: 0; top: 0; width: 300px; height: 240px; }
  .letterhead .wash--low { left: 0; top: 455px; width: 280px; height: 225px; }
  .letterhead .wordmark { left: 69px; top: 120px; font-size: 22px; }
  .letterhead .wordmark__dot { width: 12px; height: 12px; }
  .letter-body {
    position: absolute; left: 69px; top: 240px; width: 345px;
    font-size: 9.3px; line-height: 1.27; color: var(--ink);
  }
  .letter-body p + p { margin-top: 10px; }
  .signature {
    position: absolute; left: 338px; top: 482px; width: 80px; height: 20px;
    background: linear-gradient(90deg, rgba(43,43,43,.12), rgba(43,43,43,.03));
    border-radius: 10px;
  }
  .sign-off {
    position: absolute; right: 68px; top: 520px; text-align: right;
    font-size: 9.5px; line-height: 1.2;
  }
  .sign-off .role { font-size: 8px; }
  .sign-off .mail { margin-top: 14px; font-size: 9px; }
  .letter-footer {
    position: absolute; left: 0; right: 0; bottom: 0; height: 43px;
    border-top: 2px solid var(--brand-green);
    text-align: center; font-size: 6.2px; line-height: 1.7; padding-top: 8px;
    color: var(--ink-soft); background: var(--paper);
  }

  /* Business cards */
  .card { width: 247px; height: 159px; left: 643px; }
  .card--front { top: 185px; }
  .card--back { top: 373px; }
  .card .wash--corner { right: 0; top: 0; width: 190px; height: 159px; }
  .card--front .wordmark { left: 28px; top: 73px; font-size: 17px; }
  .card--front .wordmark__dot { width: 9px; height: 9px; }
  .card-address {
    position: absolute; right: 20px; top: 20px; text-align: right;
    font-size: 7.5px; line-height: 1.4; color: var(--ink-soft);
  }
  .card-person { position: absolute; left: 21px; top: 50px; }
  .card-person .name { color: var(--brand-blue); font-size: 11.5px; font-weight: 500; }
  .card-person .role { font-size: 9px; }
  .card-person .mail { margin-top: 14px; font-size: 10px; }
  .card-contact {
    position: absolute; right: 20px; top: 108px; text-align: right;
    font-size: 7.5px; line-height: 1.55; color: var(--ink-soft);
  }

  /* Compliment slip */
  .slip { left: 616px; top: 640px; width: 478px; height: 224px; }
  .slip .wash--corner { right: 0; top: 0; width: 290px; height: 190px; }
  .slip .wordmark { left: 30px; top: 34px; font-size: 17px; }
  .slip .wordmark__dot { width: 9px; height: 9px; }
  .slip-greeting {
    position: absolute; left: 29px; top: 168px;
    font-size: 9.5px; color: var(--brand-green);
  }
  .slip-footer {
    position: absolute; left: 0; right: 0; bottom: 0; height: 36px;
    background: var(--brand-green); text-align: center;
    font-size: 7.5px; line-height: 1.45; padding-top: 7px; color: #5e8f35;
  }
</style>
</head>
<body>

<section class="sheet letterhead" aria-label="Letterhead">
  <div class="wash wash--corner" role="img" aria-label="Soft green and lavender corner gradient"></div>
  <div class="wash wash--low" role="img" aria-label="Soft lavender and green gradient"></div>
  <div class="wordmark"><span>Vorn-Q</span><span class="wordmark__dot"></span></div>
  <div class="letter-body">
    <p>Quid magni cus dolumque doluptio eatur? Denitas dus, quo quiae volo dolorpos unt, te nobitem sequo et et as earibus veriaectatis doluptisque vero et quidenis sin ni qui te volorro bea inciendaeces secat et plit, oc-cum is dolorectotat verita conseriores dolore coribusdae atibustia veri ut del ius quod unt.</p>
    <p>Hicae voluptas mil ipit officil maiorrore perro ommodi volor sedit aut idellest, sunt ut aliquae et et ut occum iur sitis millatures exceate sserectempor suntiam, ium ullest, que nonsedi aliqui temquid quiatia ne vere porem aut endio blanda sus, sercips aniaspiet aliatissi duntem que que dus ea quidi arum ut labor antem volor min nem quist alibus, comnist, quis debitas magnis moluptatiae parum vendae sandempos de corporpore seceriosam fugiamus exeriatem quae pa ilit eiusaes tiatur se cuptaquam que reptatentes ex estrund usdandios pe vitae.</p>
    <p>Quunt est harunt, quo dollique cusdae que sit que nusapic iaspedis et quidicium et eatemqui inciasseque estiunt es et laccum dolor acimus cus sitibustrum eum quuntis.</p>
  </div>
  <div class="signature" role="img" aria-label="Handwritten signature"></div>
  <div class="sign-off">
    <div class="name">Dan Price</div>
    <div class="role">Director</div>
    <div class="mail">dan@vorn-q.example</div>
  </div>
  <footer class="letter-footer">
    <div>Vorn-Q Ltd. • 62-78 Harrowfield Lane London N7 3RB • 020 7915 3381 • www.vorn-q.example • info@vorn-q.example</div>
    <div>Company is Registered in England and Wales Company No. 06513249</div>
  </footer>
</section>

<section class="sheet card card--front" aria-label="Business card front">
  <div class="wash wash--corner" role="img" aria-label="Soft green and lavender corner gradient"></div>
  <div class="wordmark"><span>Vorn-Q</span><span class="wordmark__dot"></span></div>
</section>

<section class="sheet card card--back" aria-label="Business card back">
  <div class="wash wash--corner" role="img" aria-label="Soft green and lavender corner gradient"></div>
  <div class="card-address">62-78 Harrowfield Lane<br>London N7 3RB</div>
  <div class="card-person">
    <div class="name">Dan Price</div>
    <div class="role">Director</div>
    <div class="mail">dan@vorn-q.example</div>
  </div>
  <div class="card-contact">020 7915 3381<br>www.vorn-q.example<br>info@vorn-q.example</div>
</section>

<section class="sheet slip" aria-label="Compliment slip">
  <div class="wash wash--corner" role="img" aria-label="Soft green and lavender corner gradient"></div>
  <div class="wordmark"><span>Vorn-Q</span><span class="wordmark__dot"></span></div>
  <div class="slip-greeting">With compliments</div>
  <footer class="slip-footer">
    <div>Vorn-Q Ltd. • 62-78 Harrowfield Lane London N7 3RB • 020 7915 3381 • www.vorn-q.example • info@vorn-q.example</div>
    <div>Company is Registered in England and Wales Company No. 06513249</div>
  </footer>
</section>

</body>
</html>
```